Resume for CEO

I need two formats of a resume created.

#1. It is 3 pages long and is the extended version.

#2. Is the 1 page resume.

Both should have the same styling. I am attaching the long and short version in word. I am also attaching a temporary picture for the resume. I will switch that out myself. Don't worry about keeping the sizing. It can be whatever you want.

There is a good website to use as a reference. http://brindlecvs.com/
The reason I am not using this site is because they don't give you the files for editing. They make you use them to edit.

Please feel free to ask questions. I"m excited to see the ideas that come up.

End format should be in AI with PDF's. I want 1 resume that is 3-4 pages and one that is 1 page. They should have the same style.

Dale

Reason: I have only received 2 designs. Hopefully I can get more submissions.

Reason: I need to get the design finalized and I will end the project.

```html
<!DOCTYPE html>
<html lang="en">
<head>
<meta charset="utf-8">
<title>Dale R. Hartwell – Resume</title>
<link href="https://fonts.googleapis.com/css2?family=Anton&family=Caladea:wght@400;700&family=Carlito:wght@400;700&family=Amarante&display=swap" rel="stylesheet">
<style>
  :root{
    --bg-tan:#d4bf98;
    --bg-light:#fbf8f2;
    --bar-brown:#7a4a26;
    --bar-brown-dark:#5e3518;
    --frame-brown:#6b3a12;
    --pill-fill:#ebe6a4;
    --card-tan:#c6b08a;
    --arrow-grey:#555555;
    --arrow-shadow:#b9b9b9;
    --ink:#1a1a1a;
    --name-yellow:#f6e21a;
    --white:#ffffff;
  }
  html,body{margin:0;padding:0;overflow:hidden;}
  body{width:848px;height:1200px;}
  .resume{
    position:relative;width:848px;height:1200px;overflow:hidden;
    background:linear-gradient(90deg,var(--bg-tan) 0%,#e6d7bb 30%,var(--bg-light) 62%,#e4d4b5 82%,var(--bg-tan) 100%);
    font-family:"Caladea",serif;color:var(--ink);
  }
  .side-bar{
    position:absolute;left:47px;top:0;width:223px;height:1220px;
    background:linear-gradient(90deg,var(--bar-brown-dark),var(--bar-brown) 20%,var(--bar-brown) 80%,var(--bar-brown-dark));
    border-radius:40px;
  }
  .portrait{
    position:absolute;left:29px;top:47px;width:252px;height:287px;
    background:var(--white);box-shadow:6px 6px 0 #9a9a9a;
  }
  .portrait-fill{
    position:absolute;left:7px;top:7px;right:7px;bottom:7px;
    background:linear-gradient(135deg,#8a6a3a 0%,#b89562 35%,#4a4f5a 70%,#3a3e46 100%);
  }
  .owner-name{
    position:absolute;left:26px;top:393px;margin:0;
    font-family:"Anton",sans-serif;font-weight:400;font-size:34px;letter-spacing:1px;
    color:var(--name-yellow);transform:scaleY(1.1);
    -webkit-text-stroke:1.5px var(--bar-brown-dark);
    text-shadow:2px 2px 0 #fff8c8;
  }
  .section-arrow{position:absolute;}
  .section-arrow span{
    position:absolute;left:0;font-family:"Carlito",sans-serif;font-weight:700;
    color:var(--white);font-size:19px;line-height:1.25;
  }
  .title-tab{
    position:absolute;background:var(--white);
    border:2px solid #222;border-right-width:5px;border-top-width:4px;
    box-shadow:0 -4px 0 #999 inset;box-sizing:border-box;
    display:flex;align-items:center;padding:0 10px;
  }
  .title-tab h2,.title-tab h3{margin:0;}
  .headline{font-family:"Caladea",serif;font-weight:700;font-size:20px;letter-spacing:.3px;}
  .job-title{font-family:"Carlito",sans-serif;font-weight:700;font-size:20px;}
  .job-dates{font-family:"Carlito",sans-serif;font-size:14px;margin-left:auto;}
  .pill{
    position:absolute;box-sizing:border-box;background:var(--pill-fill);
    border:4px solid var(--frame-brown);border-radius:22px;
    box-shadow:0 0 0 3px #f6efd8,0 0 0 6px var(--frame-brown);
  }
  .profile-text{
    margin:0;padding:18px 18px;font-size:13.3px;line-height:1.34;text-align:justify;
  }
  .job-text{margin:0;padding:8px 14px;font-size:13.3px;line-height:1.3;}
  .job-place{
    display:block;text-align:center;font-family:"Carlito",sans-serif;font-style:italic;
    text-decoration:underline;font-size:13.5px;margin-top:2px;
  }
  .school-tab{justify-content:flex-start;padding-left:18px;}
  .school-tab h3{font-family:"Carlito",sans-serif;font-weight:700;font-size:19px;}
  .school-tab h3::before{content:"•";margin-right:24px;}
  .study{
    margin:0;font-family:"Carlito",sans-serif;font-size:14.5px;line-height:1.6;
    padding:6px 20px 6px 48px;position:relative;
  }
  .study::before{content:"⇨";position:absolute;left:18px;}
  .connectors{position:absolute;left:0;top:0;pointer-events:none;}
  .contact-card{
    position:absolute;left:14px;top:826px;width:308px;height:292px;box-sizing:border-box;
    background:var(--card-tan);border:6px solid var(--white);
    box-shadow:3px 4px 6px rgba(0,0,0,.35);
    clip-path:polygon(0 0,100% 0,100% 88%,90% 100%,0 100%);
  }
  .contact-card h2{
    margin:22px 0 30px;text-align:center;font-family:"Amarante",serif;font-weight:400;
    font-size:30px;text-decoration:underline;
  }
  .contact-line{margin:0 0 22px 2px;font-family:"Amarante",serif;font-size:15.5px;font-weight:700;}
  .contact-line .indent{display:block;padding-left:68px;}
</style>
</head>
<body>
<main class="resume">
  <div class="side-bar"></div>

  <div class="portrait">
    <div class="portrait-fill" role="img" aria-label="Portrait photo of the candidate in a dark suit jacket"></div>
  </div>

  <h1 class="owner-name">DALE R.HARTWELL</h1>

  <svg class="connectors" width="848" height="1200" aria-hidden="true">
    <g stroke="#111" stroke-width="1.5" fill="#111">
      <line x1="327" y1="253" x2="307" y2="253"/><circle cx="327" cy="253" r="4"/>
      <line x1="242" y1="325" x2="325" y2="325"/><line x1="325" y1="325" x2="325" y2="320"/><circle cx="242" cy="325" r="4"/><circle cx="325" cy="320" r="3.5"/>
      <line x1="242" y1="617" x2="330" y2="617"/><circle cx="242" cy="617" r="4"/><circle cx="330" cy="617" r="3.5"/>
      <line x1="242" y1="762" x2="327" y2="762"/><circle cx="242" cy="762" r="4"/><circle cx="327" cy="762" r="3.5"/>
      <line x1="327" y1="1005" x2="398" y2="1005"/><circle cx="398" cy="1005" r="3.5"/>
      <line x1="250" y1="1118" x2="398" y2="1118"/><circle cx="398" cy="1118" r="3.5"/>
    </g>
  </svg>

  <!-- Profile -->
  <div class="section-arrow" style="left:281px;top:14px;width:190px;height:120px;">
    <svg width="190" height="120" aria-hidden="true">
      <polygon points="30,38 128,38 128,14 178,64 128,114 128,92 30,92" fill="var(--arrow-shadow)"/>
      <polygon points="10,50 115,50 115,20 180,76 115,132 115,102 10,102" fill="var(--arrow-shadow)" transform="translate(0,-14)"/>
      <polygon points="10,40 115,40 115,18 165,66 115,114 115,92 10,92" fill="var(--arrow-grey)"/>
    </svg>
    <span style="left:48px;top:54px;">Profile</span>
  </div>

  <div class="title-tab" style="left:331px;top:138px;width:475px;height:44px;">
    <h2 class="headline">CHIEF EXECUTIVE OFFICER &amp; ENTREPRENEUR</h2>
  </div>
  <div class="pill" style="left:307px;top:185px;width:527px;height:196px;">
    <p class="profile-text">Dynamic Chief Executive Officer with over 16 years of experience in providing strategic direction and leadership for organizations in multiple markets with unique situations. Extensive experience transforming companies into profitable and progressive organizations using proven systematic implementation. Offers comprehensive knowledge and operational experience with highly-engineered technical manufacturing companies, ecommerce and international brand building. Effectively identifies critical business drivers in multiple markets and industries, enabling growth opportunities within a variety of departments and ultimately complete business expansion.</p>
  </div>

  <!-- Professional Experience -->
  <div class="section-arrow" style="left:269px;top:390px;width:215px;height:145px;">
    <svg width="215" height="145" aria-hidden="true">
      <polygon points="20,30 140,30 140,4 205,70 140,136 140,104 20,104" fill="var(--arrow-shadow)"/>
      <polygon points="0,38 128,38 128,10 190,74 128,138 128,110 0,110" fill="var(--arrow-grey)"/>
    </svg>
    <span style="left:34px;top:50px;">Professional<br>&nbsp;&nbsp;Experience</span>
  </div>

  <div class="title-tab" style="left:337px;top:533px;width:471px;height:42px;">
    <h3 class="job-title">Interim Chief Executive Officer</h3>
    <span class="job-dates">(August 2013—January 2014)</span>
  </div>
  <div class="pill" style="left:310px;top:574px;width:527px;height:88px;">
    <p class="job-text">Provides strategic direction as Interim CEO for this innovative gourmet food truck company aiming to be first publicly traded food truck company in the United States
      <span class="job-place">Melted Wheel Truck Co., LLC: Austin, TX &nbsp;(www.meltedwheeltruck.example)</span></p>
  </div>

  <div class="title-tab" style="left:343px;top:679px;width:467px;height:42px;">
    <h3 class="job-title">Chief Executive Officer</h3>
    <span class="job-dates">(May 2009 - November 2011)</span>
  </div>
  <div class="pill" style="left:310px;top:724px;width:527px;height:102px;">
    <p class="job-text">Turned this ailing specialty bicycle company around through rebranding effort s and Improved marketing and sales strategy ,accelerating to profitable state within 12 months .
      <span class="job-place">Brightline Handbuilt Cycles, Inc.: San Diego, CA &nbsp;(www.brightlinecycles.example)</span></p>
  </div>

  <!-- Contact -->
  <section class="contact-card">
    <h2>Contact</h2>
    <p class="contact-line">E-mail : dalehartwell22@mailbox.example</p>
    <p class="contact-line">Phone : (555) 014 - 2290</p>
    <p class="contact-line">Address : 4810 Cedar Ridge Rd.<span class="indent">Ste.210</span></p>
  </section>

  <!-- Education -->
  <div class="section-arrow" style="left:326px;top:830px;width:190px;height:115px;">
    <svg width="190" height="115" aria-hidden="true">
      <polygon points="20,26 130,26 130,4 185,54 130,104 130,82 20,82" fill="var(--arrow-shadow)"/>
      <polygon points="0,32 118,32 118,8 170,60 118,112 118,88 0,88" fill="var(--arrow-grey)"/>
    </svg>
    <span style="left:14px;top:47px;">EDUCATION</span>
  </div>

  <div class="title-tab school-tab" style="left:410px;top:937px;width:363px;height:46px;">
    <h3>Westbrook University</h3>
  </div>
  <div class="pill" style="left:378px;top:983px;width:416px;height:50px;">
    <p class="study">General Studies &amp; pre-med</p>
  </div>

  <div class="title-tab school-tab" style="left:410px;top:1036px;width:363px;height:46px;">
    <h3>Pacific Coast State University</h3>
  </div>
  <div class="pill" style="left:378px;top:1081px;width:416px;height:72px;">
    <p class="study">Bachelor of Science in Business Aministration/ Marketing</p>
  </div>
</main>
</body>
</html>
```